Label for flatbread

create an innovative and visually appealing label for flatbread packaging. The goal is to blend traditional bread-making heritage with a modern aesthetic that attracts consumers in retail environments while communicating freshness, quality, and authenticity.

To design a front-facing package label for flatbread that:
• Captures the essence of artisanal baking and cultural tradition.
• Stands out on shelves with strong visual appeal.
• You can use folk art to create the images on the label, elements like flatbread, wheat,
We want to print the label in a sticker and put it on bread bag, so consider that you are designing a label in a frame for instance 4 inch in 5 inch rectangular. We would like that the label has theme like the uploaded images (does not need to be similar to the uploaded images) these images give you a clue .

Target Market(s)

Groceries stores in Vancouver area Canada

Industry/Entity Type

Bakery

Font styles to use
Other font styles liked:
• feel free to choose your font yourself

Requirements
Must have
• Design the label to attract consumers and encourage them to choose this bread. Create an eye-catching label that entices consumers to try this bread. Make the label so appealing that consumers can’t resist picking up this bread.
Nice to have
• Clean, Illustration or icon of flatbread, Subtle grain (whole wheat!) or flour textures in the background to suggest craftsmanship, Made in Canada
Should not have
• we do not limit artists, use your imagination, do not put bread picture, the bread picture must be hand drawn

```html
<!DOCTYPE html>
<html lang="en">
<head>
<meta charset="utf-8">
<title>Flat Bread Label</title>
<link href="https://fonts.googleapis.com/css2?family=Oswald:wght@600&family=Zilla+Slab:wght@400;700&display=swap" rel="stylesheet">
<style>
  :root {
    --page-bg: #ffffff;
    --label-bg: #fdf4e6;
    --label-edge: #d9cfc2;
    --ink-brown: #6b3a22;
    --ink-dark: #4a3326;
    --rule: #5a463a;
    --bread-light: #f4dc8e;
    --bread-mid: #e8ba5c;
    --bread-deep: #c9903c;
    --script-tone: #eadbc5;
  }
  html, body {
    margin: 0;
    padding: 0;
    width: 1200px;
    height: 850px;
    overflow: hidden;
    background: var(--page-bg);
  }
  .canvas {
    position: relative;
    width: 1200px;
    height: 850px;
  }
  .label {
    position: absolute;
    left: 353px;
    top: 114px;
    width: 494px;
    height: 621px;
    display: block;
  }
  .label-face { fill: var(--label-bg); stroke: var(--label-edge); stroke-width: 0.6; }
  .title {
    font-family: "Oswald", "Arial Narrow", sans-serif;
    font-weight: 600;
    font-size: 43px;
    letter-spacing: 1px;
    fill: var(--ink-brown);
  }
  .origin {
    font-family: "Zilla Slab", Georgia, serif;
    font-size: 16px;
    fill: var(--ink-dark);
  }
  .variety {
    font-family: "Zilla Slab", Georgia, serif;
    font-weight: 700;
    font-size: 15px;
    letter-spacing: 0.3px;
    fill: var(--ink-dark);
  }
  .detail {
    font-family: "Zilla Slab", Georgia, serif;
    font-size: 10.5px;
    fill: var(--ink-dark);
  }
  .rule {
    stroke: var(--rule);
    stroke-width: 0.7;
    stroke-dasharray: 2.4 1.6;
    fill: none;
  }
</style>
</head>
<body>
<div class="canvas">
  <svg class="label" viewBox="0 0 296 372" xmlns="http://www.w3.org/2000/svg">
    <defs>
      <path id="title-arc" d="M 38 98 Q 152 56 266 98"/>
      <radialGradient id="bread-tone" cx="48%" cy="42%" r="62%">
        <stop offset="0%" stop-color="var(--bread-light)"/>
        <stop offset="60%" stop-color="var(--bread-mid)"/>
        <stop offset="100%" stop-color="var(--bread-deep)"/>
      </radialGradient>
    </defs>

    <rect class="label-face" x="0.5" y="0.5" width="295" height="371"/>

    <text class="title"><textPath href="#title-arc" startOffset="50%" text-anchor="middle">FLAT BREAD</textPath></text>

    <rect class="bread-illustration" x="84" y="108" width="150" height="115" rx="48" fill="url(#bread-tone)" role="img" aria-label="Hand-drawn folk-style illustration of two stacked golden flatbreads"/>

    <text class="origin" x="148" y="250" text-anchor="middle">Made in Canada</text>
    <line class="rule" x1="32" y1="261" x2="265" y2="261"/>

    <text class="variety" x="148" y="284" text-anchor="middle">Whole Wheat</text>
    <line class="rule" x1="32" y1="297" x2="265" y2="297"/>

    <rect class="no-sugar-lettering" x="59" y="303" width="70" height="35" rx="6" fill="var(--script-tone)" role="img" aria-label="Hand lettering: No added sugar"/>

    <line class="rule" x1="157" y1="299" x2="157" y2="347"/>
    <text class="detail" x="211" y="314" text-anchor="middle">7 oz. (198 g)</text>
    <line class="rule" x1="157" y1="322" x2="265" y2="322"/>
    <text class="detail" x="211" y="338" text-anchor="middle">Baked locally</text>
    <line class="rule" x1="32" y1="347" x2="265" y2="347"/>
  </svg>
</div>
</body>
</html>
```